Webdesign Metall- und Stahlbau Harkenfeld GmbH
Zielgruppe
Metall- und Stahlbau Harkenfeld GmbH
Zielgruppe: öffentlicher Bereich, Industrie, Gesundheitswesen > deutschlandweit tätig
Aufgabenstellung
keine bewegten Bilder oder Elemente in der Website
klassisches Layout
sehr konservativ

```html
<!DOCTYPE html>
<html lang="de">
<head>
<meta charset="utf-8">
<title>Metall- und Stahlbau Harkenfeld GmbH</title>
<link href="https://fonts.googleapis.com/css2?family=Oswald:wght@500;600&family=Open+Sans:wght@400;600&display=swap" rel="stylesheet">
<style>
  :root {
    --navy: #1b3a5c;
    --navy-active: #2d5079;
    --ink: #1f2f45;
    --text: #2b2b2b;
    --muted: #4a4a4a;
    --footer: #474849;
    --page: #ffffff;
    --backdrop: #eceef1;
    --steel-dark: #2c3a4c;
    --steel-mid: #5b6d82;
    --steel-light: #a9b6c4;
  }
  * { box-sizing: border-box; margin: 0; padding: 0; }
  html, body { width: 1200px; height: 1200px; overflow: hidden; }
  body {
    background: var(--backdrop);
    font-family: "Open Sans", Arial, sans-serif;
    color: var(--text);
  }
  .site {
    position: absolute; left: 0; top: 85px;
    width: 1200px; height: 1030px;
    background: var(--page);
  }
  .site-header { position: absolute; left: 0; top: 0; width: 100%; height: 139px; }
  .brand-mark {
    position: absolute; left: 34px; top: 38px;
    width: 66px; height: 66px; background: var(--ink);
  }
  .brand-name {
    position: absolute; left: 135px; top: 42px;
    font-family: "Oswald", sans-serif; font-weight: 600;
    font-size: 28px; letter-spacing: 0.3px; color: var(--navy);
    text-transform: uppercase;
  }
  .brand-tagline {
    position: absolute; left: 136px; top: 92px;
    font-size: 18px; color: var(--muted);
  }
  .main-nav {
    position: absolute; left: 0; top: 139px; width: 100%; height: 59px;
    background: var(--navy);
    display: flex; align-items: stretch;
  }
  .main-nav a {
    display: flex; align-items: center; padding: 0 24px;
    font-family: "Oswald", sans-serif; font-weight: 500;
    font-size: 17px; color: #fff; text-decoration: none; letter-spacing: 0.2px;
  }
  .main-nav a.is-active { background: var(--navy-active); }
  .hero-photo {
    position: absolute; left: 0; top: 241px; width: 619px; height: 418px;
    background: linear-gradient(135deg, var(--steel-mid) 0%, var(--steel-dark) 55%, #3c4d63 100%);
  }
  .hero-title {
    position: absolute; left: 656px; top: 322px; width: 520px;
    font-family: "Oswald", sans-serif; font-weight: 600;
    font-size: 42px; line-height: 1.2; color: var(--navy);
    text-transform: uppercase; letter-spacing: 0.5px;
  }
  .hero-text {
    position: absolute; left: 656px; top: 482px; width: 520px;
    font-size: 18.5px; line-height: 1.45; color: var(--text);
  }
  .sector {
    position: absolute; top: 705px; width: 234px; text-align: center;
  }
  .sector-photo { width: 234px; height: 177px; }
  .sector-photo.public { background: linear-gradient(180deg, #b6c2cf 0%, #6f8194 60%, #3e4c5c 100%); }
  .sector-photo.health { background: linear-gradient(180deg, #9fc0de 0%, #e4e7ea 55%, #8fa27c 100%); }
  .sector-photo.industry { background: linear-gradient(180deg, #8d99a6 0%, #c9ced4 50%, #5c6670 100%); }
  .sector-label {
    margin-top: 19px;
    font-family: "Oswald", sans-serif; font-weight: 500;
    font-size: 18px; color: var(--ink); text-transform: uppercase;
  }
  .site-footer {
    position: absolute; left: 0; top: 973px; width: 100%; height: 57px;
    background: var(--footer);
    display: flex; align-items: center; justify-content: center; gap: 14px;
    font-family: "Oswald", sans-serif; font-weight: 500;
    font-size: 17px; color: #fff; text-transform: uppercase;
  }
  .site-footer .sep { color: #cfcfcf; }
</style>
</head>
<body>
  <div class="site">
    <header class="site-header">
      <div class="brand-mark"></div>
      <div class="brand-name">Metall- und Stahlbau Harkenfeld GmbH</div>
      <div class="brand-tagline">Meisterbetrieb seit 1965</div>
    </header>

    <nav class="main-nav">
      <a class="is-active">HOME</a>
      <a>LEISTUNGEN</a>
      <a>REFERENZEN</a>
      <a>STELLENANGEBOTE</a>
      <a>AKTUELLE MELDUNGEN</a>
      <a>DOWNLOAD</a>
      <a>DOWNLOAD</a>
      <a>UNTERNEHMENSVORSTELLUNG</a>
    </nav>

    <div class="hero-photo" role="img" aria-label="Foto: zwei Stahlbauer mit Schutzhelm schleifen einen Stahlträger in der Werkhalle, Funkenflug"></div>
    <h1 class="hero-title">Verlässlichkeit.<br>Erfahrung. Kompetenz.</h1>
    <p class="hero-text">Ihr Partner für anspruchsvolle Metall- und Stahlbauprojekte in ganz Deutschland. Seit 1965 stehen wir für Präzision und ingenieurtechnische Meisterleistungen für öffentliche Hand, Industrie und Gesundheitswesen.</p>

    <div class="sector" style="left:210px">
      <div class="sector-photo public" role="img" aria-label="Foto: stählerne Fachwerkbrücke über einem Fluss"></div>
      <div class="sector-label">Öffentliche Hand</div>
    </div>
    <div class="sector" style="left:484px">
      <div class="sector-photo health" role="img" aria-label="Foto: modernes Klinikgebäude mit Glasfassade"></div>
      <div class="sector-label">Gesundheitswesen</div>
    </div>
    <div class="sector" style="left:757px">
      <div class="sector-photo industry" role="img" aria-label="Foto: Innenansicht einer großen Industriehalle"></div>
      <div class="sector-label">Industrie</div>
    </div>

    <footer class="site-footer">
      <span>Impressum</span><span class="sep">|</span>
      <span>Datenschutz</span><span class="sep">|</span>
      <span>BFSG</span><span class="sep">|</span>
      <span>© 2026 Metall- und Stahlbau Harkenfeld GmbH</span>
    </footer>
  </div>
</body>
</html>
```